TovaLamarpe - Israeli Mental Health Website

We are developing an Israeli website for mental health. The website will be both in English and in Hebrew. We have a logo and would like a website design based on the logo and the logos colors (attached).

Attached is a doc that contains the website requirements.

We would like to have an icon for each of the sidebar categories, an image for each of the pages (including each of the sidebar category pages).

Target Market(s)

Adults 18-80

Industry/Entity Type

Mental Health

Number of Pages Required

5+ page

Font styles to use
Sans Serif

Colors

Designer to choose colors to be used in the design.

```html
<!DOCTYPE html>
<html lang="en">
<head>
<meta charset="utf-8">
<title>TovaLamarpe – Mental Health</title>
<link href="https://fonts.googleapis.com/css2?family=Fira+Sans:wght@400;500;600;700&family=Open+Sans:wght@400;600;700&display=swap" rel="stylesheet">
<style>
:root{
  --green:#4aa33e;
  --blue:#1f6fc0;
  --blue-deep:#0d47b5;
  --ink:#3d3d3d;
  --text:#555;
  --line:#4aa33e;
  --icon:#444;
  --black:#000;
  --white:#fff;
}
*{margin:0;padding:0;box-sizing:border-box}
html,body{width:1200px;height:3320px;overflow:hidden;background:var(--white)}
body{position:relative;font-family:"Open Sans",Arial,sans-serif;color:var(--text)}
.abs{position:absolute}
/* header */
.site-header{position:absolute;left:0;top:0;width:1200px;height:106px;background:var(--white)}
.brand{position:absolute;left:100px;top:34px;display:flex;align-items:center;gap:10px;font-family:"Fira Sans",sans-serif;font-weight:600;font-size:26px;color:var(--blue)}
.brand-dot{width:34px;height:34px;border-radius:50%;background:var(--blue)}
.main-nav a{position:absolute;top:45px;font-size:13px;color:#222;text-decoration:none;white-space:nowrap}
.lang{position:absolute;left:1012px;top:43px;font-family:"Fira Sans",sans-serif;font-size:16px;font-weight:500;color:#222}
.lang-flag{position:absolute;left:1072px;top:42px;width:22px;height:22px;border-radius:50%;border:2px solid var(--blue);background:#fff}
/* hero */
.hero-photo{position:absolute;left:0;top:106px;width:1200px;height:520px;
  background:
    radial-gradient(ellipse 130px 230px at 1150px 260px,#1c1512 0%,#2b211c 60%,rgba(43,33,28,0) 100%),
    radial-gradient(ellipse 120px 150px at 580px 200px,#3a2418 0%,#4d3022 55%,rgba(77,48,34,0) 100%),
    radial-gradient(ellipse 240px 200px at 600px 470px,#7f9bb9 0%,#9bb2c9 55%,rgba(155,178,201,0) 100%),
    linear-gradient(100deg,#eef1f3 0%,#d9dfe4 35%,#e7eaec 60%,#cfd3d6 85%,#b7b0a8 100%)}
.hero-curve{position:absolute;left:0;top:500px;width:1200px;height:150px}
.hero-title{position:absolute;left:658px;top:202px;width:400px;text-align:center;font-family:"Fira Sans",sans-serif;font-weight:600;font-size:44px;color:#111;letter-spacing:.5px}
.hero-text{position:absolute;left:700px;top:262px;width:316px;text-align:center;font-size:11px;line-height:16px;color:#333}
.btn{position:absolute;display:flex;align-items:center;justify-content:center;background:var(--green);color:var(--white);font-family:"Fira Sans",sans-serif;font-weight:600;border-radius:4px 18px 4px 18px;text-decoration:none;white-space:nowrap}
/* sidebar */
.category-panel{position:absolute;left:36px;top:106px;width:338px;height:481px;background:var(--white);border:2px solid var(--blue)}
.category-panel h2{height:64px;background:var(--blue);color:var(--white);font-family:"Fira Sans",sans-serif;font-weight:500;font-size:30px;display:flex;align-items:center;padding-left:40px}
.category-list{list-style:none;padding-top:8px}
.category-list li{position:relative;height:31px;border-bottom:1px solid var(--line);display:flex;align-items:center;padding-left:14px;font-family:"Fira Sans",sans-serif;font-size:13px;color:#333}
.category-list li.active{background:var(--green);color:var(--white)}
.cat-icon{width:22px;height:22px;margin-right:20px;flex:none;fill:none;stroke:var(--icon);stroke-width:1.3;stroke-linecap:round;stroke-linejoin:round}
.active .cat-icon,.active .row-arrow{stroke:var(--white)}
.row-arrow{position:absolute;right:8px;top:8px;width:16px;height:16px;fill:none;stroke-width:1.5}
/* welcome */
.welcome-title{position:absolute;left:0;top:626px;width:1200px;text-align:center;font-family:"Fira Sans",sans-serif;font-weight:600;font-size:44px;color:var(--ink)}
.welcome-text{position:absolute;left:170px;top:694px;width:860px;text-align:center;font-size:16.5px;line-height:25px;color:#555}
/* features */
.feature-title{position:absolute;font-family:"Fira Sans",sans-serif;font-weight:700;font-size:52px;color:var(--green);white-space:nowrap}
.feature-text{position:absolute;width:480px;font-size:19.5px;letter-spacing:-.35px;line-height:22.5px;color:#333}
.photo{position:absolute;width:487px;height:317px;border-radius:6px}
.emergency-title{position:absolute;left:586px;top:885px;font-family:"Fira Sans",sans-serif;font-weight:600;font-size:44px;color:var(--blue)}
.emergency-text{position:absolute;left:588px;top:962px;width:518px;font-size:16.5px;line-height:25px;color:#555}
.emergency-art{position:absolute;left:100px;top:848px;width:430px;height:422px;border-radius:50%;
  background:
    radial-gradient(circle at 50% 40%,#d8c2b0 0%,#b79f8c 22%,rgba(183,159,140,0) 45%),
    radial-gradient(circle at 22% 75%,#3f7a3a 0%,#5f8f55 25%,rgba(95,143,85,0) 50%),
    radial-gradient(circle at 78% 75%,#4a5b78 0%,rgba(74,91,120,0) 45%),
    radial-gradient(circle at 50% 50%,#a9a49c 0%,#8b8a84 65%,#d6d6d6 100%)}
/* footer */
.footer-wave{position:absolute;left:0;top:2860px;width:1200px;height:170px}
.footer-body{position:absolute;left:0;top:3020px;width:1200px;height:147px;background:var(--black)}
.contact-item{position:absolute;top:3092px;display:flex;align-items:center;gap:12px;color:var(--white)}
.contact-icon{width:38px;height:38px;border-radius:50%;background:var(--blue-deep);display:flex;align-items:center;justify-content:center}
.contact-label{font-size:11.5px;font-weight:700;display:block}
.contact-value{font-size:15px;display:block;margin-top:2px}
.footer-nav{position:absolute;left:0;top:3167px;width:1200px;height:68px;background:var(--blue-deep);display:flex;justify-content:center;align-items:center;gap:40px}
.footer-nav a{color:var(--white);font-family:"Fira Sans",sans-serif;font-weight:600;font-size:16px;text-decoration:none}
.footer-bottom{position:absolute;left:0;top:3235px;width:1200px;height:85px;background:var(--black);color:var(--white);font-family:"Fira Sans",sans-serif;font-size:14px}
.copyright{position:absolute;left:78px;top:22px}
.legal{position:absolute;left:945px;top:22px}
</style>
</head>
<body>

<header class="site-header">
  <div class="brand"><span class="brand-dot"></span>TovaLamarpe</div>
  <nav class="main-nav">
    <a style="left:334px">Smart Chatline</a>
    <a style="left:470px">therapists</a>
    <a style="left:567px">Organizations</a>
    <a style="left:687px">Videos</a>
    <a style="left:762px">Contact</a>
    <a style="left:843px">About</a>
    <a style="left:914px">Donate</a>
  </nav>
  <span class="lang">ENG ⌄</span>
  <span class="lang-flag"></span>
</header>

<div class="hero-photo" role="img" aria-label="Photo of a young man speaking with a therapist"></div>
<svg class="hero-curve" viewBox="0 0 1200 150" aria-hidden="true">
  <path d="M0 120 Q620 -30 1200 110 L1200 150 L0 150Z" fill="#fff"/>
  <path d="M374 42 Q800 -10 1135 110" fill="none" stroke="#4aa33e" stroke-width="7"/>
  <path d="M45 138 Q430 20 855 82" fill="none" stroke="#1f6fc0" stroke-width="5"/>
</svg>
<h1 class="hero-title">TOVA LAMARPE</h1>
<p class="hero-text">Lorem ipsum dolor sit amet, consectetur adipiscing elit, sed do eiusmod tempor incididunt ut labore et dolore magna aliqua. Ut enim ad minim veniam, quis nostrud exercitation ullamco laboris nisi ut aliquip ex ea</p>
<a class="btn" style="left:800px;top:343px;width:151px;height:51px;font-size:17px">Get Started</a>

<aside class="category-panel">
  <h2>Choose A Category</h2>
  <ul class="category-list">
    <li><svg class="cat-icon" viewBox="0 0 22 22"><path d="M6 16 V10 A5 5 0 0 1 16 10 V16"/><path d="M4 18 H18"/><path d="M11 2 V4 M4 6 L5.5 7.5 M18 6 L16.5 7.5"/></svg>Emergency Mental Help</li>
    <li class="active"><svg class="cat-icon" viewBox="0 0 22 22"><path d="M7 19 V15 A7 7 0 1 1 16 14 V19"/><circle cx="11" cy="9" r="2.5"/></svg>Suicide<svg class="row-arrow" viewBox="0 0 16 16"><path d="M3 8 A5 5 0 0 1 12 5 M12 2 V5 H9"/><path d="M13 8 A5 5 0 0 1 4 11 M4 14 V11 H7"/></svg></li>
    <li><svg class="cat-icon" viewBox="0 0 22 22"><path d="M11 3 L18 6 V11 C18 15 15 18 11 19 C7 18 4 15 4 11 V6 Z"/><path d="M8 11 L10 13 L14 9"/></svg>Sexual Assault/Violence Victims</li>
    <li><svg class="cat-icon" viewBox="0 0 22 22"><path d="M11 3 L20 18 H2 Z"/><path d="M11 9 V13 M11 15.5 V16"/></svg>Sexual Assault/Violence Assaulters</li>
    <li><svg class="cat-icon" viewBox="0 0 22 22"><path d="M12 2 L5 12 H10 L9 20 L17 9 H12 Z"/></svg>Post Trauma</li>
    <li><svg class="cat-icon" viewBox="0 0 22 22"><path d="M6 15 A4 4 0 0 1 6 7 A5 5 0 0 1 16 6 A4.5 4.5 0 0 1 16 15 Z"/><path d="M8 18 V20 M11 18 V20 M14 18 V20"/></svg>Depression</li>
    <li><svg class="cat-icon" viewBox="0 0 22 22"><circle cx="11" cy="11" r="8"/><path d="M11 11 m0 -4 a4 4 0 1 1 -4 4 a2 2 0 1 1 2 -2"/></svg>Anxiety</li>
    <li><svg class="cat-icon" viewBox="0 0 22 22"><path d="M7 3 H15 L14 10 A3 3 0 0 1 8 10 Z"/><path d="M11 13 V19 M7 19 H15"/></svg>Addictions</li>
    <li><svg class="cat-icon" viewBox="0 0 22 22"><path d="M15 3 A8 8 0 1 0 19 14 A6 6 0 0 1 15 3 Z"/></svg>Sleep Disorders</li>
    <li><svg class="cat-icon" viewBox="0 0 22 22"><circle cx="11" cy="12" r="6"/><path d="M3 3 V8 M5 3 V8 M4 8 V19 M19 3 C17 5 17 8 19 10 V19"/></svg>Eating Disorders</li>
    <li><svg class="cat-icon" viewBox="0 0 22 22"><circle cx="11" cy="11" r="8"/><path d="M11 6 V12 M11 15 V16"/></svg>Financial Problems</li>
    <li><svg class="cat-icon" viewBox="0 0 22 22"><circle cx="8" cy="7" r="3"/><circle cx="15" cy="10" r="2.2"/><path d="M3 19 A5 5 0 0 1 13 19 M12 19 A3.5 3.5 0 0 1 19 19"/></svg>Parenthood</li>
    <li style="border-bottom:0"><svg class="cat-icon" viewBox="0 0 22 22"><path d="M11 18 C4 13 3 10 3 8 A4 4 0 0 1 11 6 A4 4 0 0 1 19 8 C19 10 18 13 11 18 Z"/></svg>Relationship</li>
  </ul>
</aside>

<h2 class="welcome-title">WELCOME TO</h2>
<p class="welcome-text">Lorem ipsum dolor sit amet, consectetur adipiscing elit, sed do eiusmod tempor incididunt ut labore et dolore magna aliqua. Ut enim ad minim veniam, quis nostrud exercitation ullamco laboris nisi ut aliquip ex ea commodo consequat. Duis aute irure dolor in reprehenderit in voluptate velit esse cillum dolore eu fugiat nulla pariatur. Excepteur sint occaecat cupidatat non proident, sunt in culpa qui officia deserunt mollit anim id est laborum.</p>

<div class="emergency-art" role="img" aria-label="Round photo collage of a support group framed by caring hands"></div>
<h2 class="emergency-title">Emergency Mental Help</h2>
<p class="emergency-text">Lorem ipsum dolor sit amet, consectetur adipiscing elit, sed do eiusmod tempor incididunt ut labore et dolore magna aliqua. Ut enim ad minim veniam, quis nostrud exercitation ullamco laboris nisi ut aliquip ex ea commodo consequat. Duis aute irure dolor in reprehenderit in voluptate velit esse cillum dolore eu fugiat nulla pariatur. Excepteur sint occaecat cupidatat non proident, sunt in culpa qui officia deserunt mollit anim</p>
<a class="btn" style="left:588px;top:1167px;width:336px;height:50px;font-size:15px">More options for Emergency Mental Help</a>

<h2 class="feature-title" style="left:96px;top:1404px">Smart Chatline</h2>
<p class="feature-text" style="left:99px;top:1482px">Lorem ipsum dolor sit amet, consectetur adipiscing elit, sed do eiusmod tempor incididunt ut labore et dolore magna aliqua. Ut enim ad minim veniam, quis nostrud exercitation ullamco laboris nisi ut aliquip exea commodo consequat. Ut enim ad minim veniam, quis nostrud exercitation ullamco</p>
<a class="btn" style="left:99px;top:1645px;width:151px;height:51px;font-size:15px">05X-XXXXXXX</a>
<div class="photo" style="left:616px;top:1400px;background:radial-gradient(ellipse 90px 130px at 260px 170px,#d9d4cc 0%,#a99384 45%,rgba(169,147,132,0) 100%),radial-gradient(ellipse 120px 60px at 80px 40px,#8a6b4f 0%,rgba(138,107,79,0) 100%),linear-gradient(135deg,#3f3f3f,#2a2a2a 55%,#1a1a1a)" role="img" aria-label="Photo of hands holding a phone with a chat app open"></div>

<div class="photo" style="left:97px;top:1776px;background:radial-gradient(ellipse 110px 160px at 250px 170px,#6e8296 0%,rgba(110,130,150,0) 100%),radial-gradient(ellipse 90px 150px at 440px 190px,#4f5a5e 0%,rgba(79,90,94,0) 100%),radial-gradient(ellipse 90px 150px at 60px 200px,#4a4a4a 0%,rgba(74,74,74,0) 100%),linear-gradient(120deg,#bfb6a8,#e6e1d8 50%,#d2c7b8)" role="img" aria-label="Photo of a therapist with two clients in a group session"></div>
<h2 class="feature-title" style="left:626px;top:1782px">Therapists</h2>
<p class="feature-text" style="left:628px;top:1860px">Lorem ipsum dolor sit amet, consectetur adipiscing elit, sed do eiusmod tempor incididunt ut labore et dolore magna aliqua. Ut enim ad minim veniam, quis nostrud exercitation ullamco laboris nisi ut aliquip exea commodo consequat. Ut enim ad minim veniam, quis nostrud exercitation ullamco</p>
<a class="btn" style="left:628px;top:2022px;width:151px;height:52px;font-size:15px">Find Therapists</a>

<h2 class="feature-title" style="left:96px;top:2165px">Organizations</h2>
<p class="feature-text" style="left:99px;top:2243px">Lorem ipsum dolor sit amet, consectetur adipiscing elit, sed do eiusmod tempor incididunt ut labore et dolore magna aliqua. Ut enim ad minim veniam, quis nostrud exercitation ullamco laboris nisi ut aliquip exea commodo consequat. Ut enim ad minim veniam, quis nostrud exercitation ullamco</p>
<a class="btn" style="left:99px;top:2406px;width:178px;height:52px;font-size:15px">Find Organizations</a>
<div class="photo" style="left:616px;top:2160px;background:radial-gradient(ellipse 150px 70px at 250px 230px,#f2f0ec 0%,#e8d7c8 50%,rgba(232,215,200,0) 100%),radial-gradient(ellipse 160px 140px at 400px 100px,#2b2e2c 0%,rgba(43,46,44,0) 100%),linear-gradient(110deg,#8b9088,#c9ccc6 50%,#5f625e)" role="img" aria-label="Photo of hands sorting a stack of documents with colored tabs"></div>

<div class="photo" style="left:97px;top:2538px;background:radial-gradient(ellipse 160px 60px at 180px 140px,#8aa0c8 0%,rgba(138,160,200,0) 100%),radial-gradient(ellipse 90px 140px at 360px 170px,#6b5e5a 0%,rgba(107,94,90,0) 100%),linear-gradient(180deg,#2a3350 0%,#1e2a4a 50%,#34436a 100%)" role="img" aria-label="Video still of a therapy session with a play button"></div>
<svg class="abs" style="left:310px;top:2668px" width="46" height="46" viewBox="0 0 46 46" aria-hidden="true"><circle cx="23" cy="23" r="20" fill="none" stroke="#fff" stroke-width="2.5"/><path d="M18 14 L32 23 L18 32Z" fill="none" stroke="#fff" stroke-width="2.5"/></svg>
<h2 class="feature-title" style="left:626px;top:2544px">Videos</h2>
<p class="feature-text" style="left:628px;top:2622px">Lorem ipsum dolor sit amet, consectetur adipiscing elit, sed do eiusmod tempor incididunt ut labore et dolore magna aliqua. Ut enim ad minim veniam, quis nostrud exercitation ullamco laboris nisi ut aliquip exea commodo consequat. Ut enim ad minim veniam, quis nostrud exercitation ullamco</p>
<a class="btn" style="left:628px;top:2784px;width:151px;height:52px;font-size:15px">Video Library</a>

<svg class="footer-wave" viewBox="0 0 1200 170" aria-hidden="true">
  <rect width="1200" height="170" fill="#000"/>
  <path d="M0 0 H1200 V20 Q620 260 0 20 Z" fill="#fff"/>
  <path d="M60 42 Q520 190 890 100" fill="none" stroke="#4aa33e" stroke-width="7"/>
  <path d="M350 100 Q780 170 1160 0" fill="none" stroke="#1f6fc0" stroke-width="5"/>
</svg>
<div class="footer-body"></div>
<div class="contact-item" style="left:314px">
  <span class="contact-icon"><svg width="18" height="18" viewBox="0 0 18 18"><rect x="2" y="4" width="14" height="10" rx="1.5" fill="none" stroke="#fff" stroke-width="1.5"/><path d="M2.5 5 L9 10 L15.5 5" fill="none" stroke="#fff" stroke-width="1.5"/></svg></span>
  <span><span class="contact-label">CONTACT MAIL</span><span class="contact-value">info@TovaLamarpe.com</span></span>
</div>
<div class="contact-item" style="left:594px">
  <span class="contact-icon"><svg width="18" height="18" viewBox="0 0 18 18"><path d="M9 16 C5 11 4 9 4 7 A5 5 0 0 1 14 7 C14 9 13 11 9 16Z" fill="none" stroke="#fff" stroke-width="1.5"/><circle cx="9" cy="7" r="1.7" fill="#fff"/></svg></span>
  <span><span class="contact-label">OUR LOCATION</span><span class="contact-value">11 Lorem ipsum dolor sit amet 1451</span></span>
</div>
<nav class="footer-nav">
  <a>Smart Chatline</a><a>therapists</a><a>Organizations</a><a>Videos</a><a>Contact</a><a>About</a><a>Donate</a>
</nav>
<footer class="footer-bottom">
  <span class="copyright">TovaLamarpe - Organization for Mental Health ©2023</span>
  <span class="legal">Privacy Policy &nbsp;|&nbsp; Terms</span>
</footer>

</body>
</html>
```